Introduction brochure for IT Company

We need a brochure for introducing our new small business services to the market.

We need a template that we can alter and play with as services change, and was thinking about the following:

A front page which has logo (attached), and follows colour scheme used on our website www.qexdatalink.com.au, that has a small description of the service/or us, we are introducing and Call us on 1300 871 629 at the bottom of page.
For the first print only front page and back page will be used, as we are still refining the service. We will be introducing the company to new prospects face to face and want to leave them with a small brochure which explains what we do for them, and clear contact details.

Middle section we have not worked out fully yet, as it depends on space available, but please use points under service on our website for now to fill in with some points.

Last page we want to have the last 1/3 of page to be our contact details along with a google map of our location etc. like the contact us page on website.

We prefer to stay on the lighter side, so more playful in style but you guys are the experts.

Target Market(s)

Small business 1-10 Employees

Industry/Entity Type

It Company

Font styles to use
Serif

Requirements
Must have
• Clear contact details, playful design which is easy to read. Follow colour scheme or close to website, www.qexdatalink.com.au, as this is reflected in all our marketing. Some artistic license is of course given.
Nice to have
• Nothing comes to mind, go crazy and make it fun.
Should not have
• typical images of large scale server racks and enterprise level images. Stay small business.

```html
<!DOCTYPE html>
<html lang="en">
<head>
<meta charset="utf-8">
<title>Qex Datalink – Introduction Brochure</title>
<link href="https://fonts.googleapis.com/css2?family=Open+Sans:wght@400;600;700;800&family=Oswald:wght@500;700&display=swap" rel="stylesheet">
<style>
  :root{
    --red:#d5121b;
    --red-dark:#a80d14;
    --charcoal:#2a2a2b;
    --charcoal-soft:#3a3a3c;
    --paper:#ffffff;
    --ink:#3b3b3b;
    --stage:#e4e4e4;
    --muted:#cfcfcf;
  }
  *{box-sizing:border-box;margin:0;padding:0}
  html,body{width:835px;height:1200px;overflow:hidden;background:var(--stage);font-family:"Open Sans",Arial,sans-serif;color:var(--ink)}
  .spread{position:absolute;left:27px;width:780px;height:552px;display:flex;box-shadow:0 6px 18px rgba(0,0,0,.25)}
  .spread--outside{top:40px}
  .spread--inside{top:618px}
  .panel{position:relative;width:390px;height:552px;overflow:hidden}
  .panel svg.shape{position:absolute;left:0;top:0;width:390px;height:552px}
  .brand{font-family:"Open Sans",Arial,sans-serif;font-weight:800;letter-spacing:.2px;display:flex;align-items:center;gap:6px}
  .brand-dot{width:9px;height:9px;border-radius:50%;background:var(--red)}

  /* back cover */
  .back{background:var(--charcoal)}
  .back .brand{position:absolute;left:52px;top:200px;color:#fff;font-size:24px}
  .contact-list{position:absolute;left:54px;top:246px;list-style:none;color:#fff;font-size:10.5px;line-height:1.55}
  .contact-list li{display:flex;gap:7px;align-items:flex-start}
  .contact-list svg{flex:none;margin-top:3px}
  .map{position:absolute;left:236px;top:200px;width:118px;height:76px;border-radius:10px;border:3px solid #fff;outline:1.5px solid var(--red);background:linear-gradient(135deg,#e9e6df,#d9dcd6)}
  .web{position:absolute;color:#fff;font-size:11px;font-weight:600}
  .back .web{right:24px;bottom:14px}

  /* front cover */
  .front{background:var(--paper)}
  .front .brand{position:absolute;left:0;right:0;top:20px;justify-content:center;color:var(--red);font-size:24px}
  .photo{position:absolute}
  .front .photo{left:0;top:64px;width:390px;height:270px;background:linear-gradient(160deg,#7f838c 0%,#b9a89f 50%,#6f7c92 100%)}
  .tagline{position:absolute;left:0;right:0;top:372px;text-align:center;color:#fff;font-family:"Oswald",Arial,sans-serif;font-weight:700;font-size:30px;line-height:1.1;text-transform:uppercase}
  .front .web{right:24px;bottom:14px}

  /* inside */
  .inside-left,.inside-right{background:var(--paper)}
  .tab{position:absolute;top:20px;background:var(--red);color:#fff;font-family:"Oswald",Arial,sans-serif;font-weight:700;font-size:13px;padding:2px 14px;border-radius:12px;text-transform:uppercase}
  .inside-left .tab{left:22px}
  .inside-right .tab{left:20px;top:24px}
  .copy{position:absolute;font-size:6.6px;line-height:1.38;color:var(--ink)}
  .copy p{margin-bottom:5px}
  .about-copy{left:22px;top:46px;width:348px}
  .inside-left .photo{left:16px;top:330px;width:180px;height:118px;border-radius:4px;background:linear-gradient(120deg,#f1ece8,#d8c3b6 60%,#efe8e3)}
  .callout{position:absolute;left:210px;top:338px;width:165px;text-align:right}
  .callout-lead{font-size:7.5px;font-weight:700;color:var(--ink)}
  .callout-phone{font-size:22px;font-weight:800;color:var(--charcoal);margin-top:10px;letter-spacing:.3px}
  .callout-email{font-size:8px;font-weight:600}
  .callout-addr{font-size:8px;font-weight:600;line-height:1.3;margin-top:2px}
  .quote{position:absolute;left:22px;top:470px;width:346px;color:#fff;font-size:6.6px;line-height:1.4}
  .quote cite{display:block;text-align:right;color:var(--red);font-style:normal;font-weight:700;margin-top:2px}

  .services-intro{left:20px;top:50px;width:352px}
  .service-list{position:absolute;left:20px;top:70px;width:352px;list-style:none}
  .service-list li{display:flex;gap:8px;margin-bottom:5px}
  .service-list .icon{flex:none;width:14px;height:14px;margin-top:1px}
  .service-list h3{font-size:7.6px;font-weight:700;color:var(--red)}
  .service-list p{font-size:6.4px;line-height:1.35}
  .pitch{left:20px;top:345px;width:352px}
  .reasons{position:absolute;left:20px;top:393px;width:352px;list-style:none;font-size:6.6px;line-height:1.6}
  .reasons-title{font-weight:700;font-size:7px}
  .reasons li{display:flex;gap:6px;align-items:center}
  .inside-right .web{left:0;right:0;text-align:center;bottom:40px;color:var(--charcoal);font-size:12px}
</style>
</head>
<body>

<section class="spread spread--outside" aria-label="Outside spread">
  <div class="panel back">
    <svg class="shape" viewBox="0 0 390 552" aria-hidden="true">
      <path d="M0 552 L0 508 C130 500 280 470 390 428 L390 552 Z" fill="#fff"/>
      <path d="M0 552 L0 522 C140 512 285 484 390 446 L390 552 Z" fill="var(--red)"/>
    </svg>
    <div class="brand"><span>Qex Datalink</span><span class="brand-dot"></span></div>
    <ul class="contact-list">
      <li><svg width="8" height="8" viewBox="0 0 10 10"><path d="M2 0 L4 2 L3 4 C4 6 5 7 6 7 L8 6 L10 8 L8 10 C4 10 0 6 0 2 Z" fill="var(--red)"/></svg>1300 871 629</li>
      <li><svg width="9" height="7" viewBox="0 0 10 8"><rect width="10" height="8" rx="1" fill="var(--red)"/><path d="M0 1 L5 5 L10 1" stroke="#fff" fill="none"/></svg>service@qexdatalink.com.au</li>
      <li><svg width="8" height="10" viewBox="0 0 8 10"><path d="M4 10 C1 6 0 5 0 4 A4 4 0 0 1 8 4 C8 5 7 6 4 10 Z" fill="var(--red)"/><circle cx="4" cy="4" r="1.5" fill="#fff"/></svg>14/58 Marlow Street, Kelsey Park<br>TAS 7021</li>
      <li><svg width="8" height="8" viewBox="0 0 10 10"><circle cx="5" cy="5" r="5" fill="var(--red)"/><path d="M5 2 V5 H7.5" stroke="#fff" fill="none"/></svg>Monday-Friday 9am - 5pm</li>
    </ul>
    <div class="map" role="img" aria-label="Street map showing the office location"></div>
    <span class="web">www.qexdatalink.com.au</span>
  </div>

  <div class="panel front">
    <div class="brand"><span>Qex Datalink</span><span class="brand-dot"></span></div>
    <div class="photo" role="img" aria-label="Photo of a family relaxing on a sofa using a laptop and tablet"></div>
    <svg class="shape" viewBox="0 0 390 552" aria-hidden="true">
      <path d="M0 300 C140 334 270 322 390 262 L390 552 L0 552 Z" fill="var(--red)"/>
      <path d="M0 318 C140 350 275 338 390 282 L390 552 L0 552 Z" fill="var(--charcoal)"/>
      <path d="M120 552 C230 530 320 500 390 462 L390 552 Z" fill="#fff"/>
      <path d="M150 552 C250 534 330 506 390 476 L390 552 Z" fill="var(--red)"/>
    </svg>
    <h1 class="tagline">One stop shop for all<br>your IT needs</h1>
    <span class="web">www.qexdatalink.com.au</span>
  </div>
</section>

<section class="spread spread--inside" aria-label="Inside spread">
  <div class="panel inside-left">
    <svg class="shape" viewBox="0 0 390 552" aria-hidden="true">
      <path d="M0 448 C140 470 280 470 390 452" stroke="var(--red)" stroke-width="3" fill="none"/>
      <path d="M0 452 C140 474 280 474 390 456 L390 552 L0 552 Z" fill="var(--charcoal)"/>
    </svg>
    <h2 class="tab">About us</h2>
    <div class="copy about-copy">
      <p>Qex Datalink is a reliable one-stop service for all things tech and web. Specialising in computer services, IT support and internet installation, our team works with homes and small businesses around the Greater Hobart area.</p>
      <p>Qex Datalink began full time operations in August 2015, after running as a part time sole trader since 2010. Daniel, our founder, spent many years as an IT manager for a large network provider and saw how often small firms were left without fair and effective computer and IT help.</p>
      <p>Daniel decided to build on his nineteen years of experience and create a business that puts local customers first. The focus is on clear advice, honest pricing and solutions that fit each client's needs, habits and budget, so everything just works.</p>
      <p>Since going full time, demand for friendly computer and IT support has grown quickly. Customers value the fast turnaround, reliability and plain answers, and they know every job is handled with care from start to finish.</p>
      <p>Our ability to deliver modern IT support and solutions has helped many families and small offices make the most of their technology. From home users to teams of ten, we take the time to understand what each client needs and we make it easy.</p>
    </div>
    <div class="photo" role="img" aria-label="Photo of a smiling woman lying down holding a tablet"></div>
    <div class="callout">
      <p class="callout-lead">Talk to us today about what you need and get a quote, no strings attached.</p>
      <p class="callout-phone">1300 871 629</p>
      <p class="callout-email">service@qexdatalink.com.au</p>
      <p class="callout-addr">14/58 Marlow Street,<br>Kelsey Park<br>TAS 7021</p>
    </div>
    <blockquote class="quote">
      “As a computer user I only know enough to get by, and things go wrong at the worst times. Daniel has saved the day more than once, fixing the issue quickly and showing me how to avoid it in future. The service is friendly, honest and great value. I would happily recommend Qex Datalink to anyone who needs reliable help close to home.”
      <cite>Leah Morton, Kelsey Point Tasmania</cite>
    </blockquote>
  </div>

  <div class="panel inside-right">
    <svg class="shape" viewBox="0 0 390 552" aria-hidden="true">
      <path d="M0 552 L0 522 C150 534 300 518 390 494 L390 552 Z" fill="var(--red)"/>
    </svg>
    <h2 class="tab">Services</h2>
    <p class="copy services-intro">Qex Datalink provides a wide range of services to home and office users. We will visit you on site for the following:</p>
    <ul class="service-list">
      <li><svg class="icon" viewBox="0 0 14 14"><rect x="1" y="2" width="12" height="8" rx="1" fill="var(--red)"/><rect x="5" y="11" width="4" height="2" fill="var(--red)"/></svg><div><h3>Computer hardware and software installations and troubleshooting</h3><p>Whatever computer problem you face, our skilled technicians will find the cause and fix it fast so you can get back to work.</p></div></li>
      <li><svg class="icon" viewBox="0 0 14 14"><rect x="2" y="1" width="10" height="12" rx="1" fill="var(--red)"/><rect x="4" y="3" width="6" height="2" fill="#fff"/></svg><div><h3>Custom built computer service</h3><p>We build systems that match how you work, with the right parts for your tasks and budget, and no extras you will never use.</p></div></li>
      <li><svg class="icon" viewBox="0 0 14 14"><path d="M1 6 A9 9 0 0 1 13 6" stroke="var(--red)" stroke-width="1.6" fill="none"/><path d="M3.5 8.5 A5.5 5.5 0 0 1 10.5 8.5" stroke="var(--red)" stroke-width="1.6" fill="none"/><circle cx="7" cy="11.5" r="1.4" fill="var(--red)"/></svg><div><h3>Internet installations and advice</h3><p>We can advise you on the best broadband or NBN plan for your usage, then set it all up so you stay connected.</p></div></li>
      <li><svg class="icon" viewBox="0 0 14 14"><rect x="1" y="5" width="12" height="6" rx="1" fill="var(--red)"/><path d="M4 5 V2 M10 5 V2" stroke="var(--red)" stroke-width="1.5"/></svg><div><h3>Wired and wireless network installations and advice</h3><p>We can connect your home or office devices so that files, printers and internet are shared securely and simply.</p></div></li>
      <li><svg class="icon" viewBox="0 0 14 14"><ellipse cx="7" cy="3.5" rx="5.5" ry="2.2" fill="var(--red)"/><rect x="1.5" y="3.5" width="11" height="7" fill="var(--red)"/><ellipse cx="7" cy="10.5" rx="5.5" ry="2.2" fill="var(--red)"/></svg><div><h3>Data backup and recovery</h3><p>Never lose data again. We set up backups that suit your needs and help recover files when things go wrong.</p></div></li>
      <li><svg class="icon" viewBox="0 0 14 14"><path d="M7 1 L12.5 3 V7 C12.5 10 10 12 7 13 C4 12 1.5 10 1.5 7 V3 Z" fill="var(--red)"/><path d="M4.5 7 L6.3 8.8 L9.5 5.4" stroke="#fff" stroke-width="1.4" fill="none"/></svg><div><h3>Computer and network IT security services</h3><p>We check that your systems and network are protected at all times against malware, viruses and other threats.</p></div></li>
      <li><svg class="icon" viewBox="0 0 14 14"><circle cx="5" cy="4" r="2.5" fill="var(--red)"/><path d="M1 13 C1 9 9 9 9 13 Z" fill="var(--red)"/><rect x="9" y="2" width="4" height="6" fill="var(--red)"/></svg><div><h3>IT training</h3><p>We can help you learn about your hardware and software. We also offer training on any new purchase you make.</p></div></li>
    </ul>
    <p class="copy pitch">We have partnered with some of the best vendors and suppliers in the industry to be able to provide you with the best hardware and software on the market today. So do yourself a favour, call us today and get the help you have always wanted.</p>
    <ul class="reasons">
      <li class="reasons-title">Why would you choose us as your IT solution provider?</li>
      <li><svg width="8" height="7" viewBox="0 0 8 7"><path d="M1 3.5 L3 5.5 L7 1" stroke="var(--red)" stroke-width="1.6" fill="none"/></svg>No fix, no charge policy.</li>
      <li><svg width="8" height="7" viewBox="0 0 8 7"><path d="M1 3.5 L3 5.5 L7 1" stroke="var(--red)" stroke-width="1.6" fill="none"/></svg>Friendly, highly knowledgeable staff - all questions answered.</li>
      <li><svg width="8" height="7" viewBox="0 0 8 7"><path d="M1 3.5 L3 5.5 L7 1" stroke="var(--red)" stroke-width="1.6" fill="none"/></svg>We'll take care of everything from the first installation to IT support - all from one expert.</li>
      <li><svg width="8" height="7" viewBox="0 0 8 7"><path d="M1 3.5 L3 5.5 L7 1" stroke="var(--red)" stroke-width="1.6" fill="none"/></svg>Professional quality advice on the best way to use and care for your systems.</li>
      <li><svg width="8" height="7" viewBox="0 0 8 7"><path d="M1 3.5 L3 5.5 L7 1" stroke="var(--red)" stroke-width="1.6" fill="none"/></svg>Obligation-free quotes - get yours now.</li>
      <li><svg width="8" height="7" viewBox="0 0 8 7"><path d="M1 3.5 L3 5.5 L7 1" stroke="var(--red)" stroke-width="1.6" fill="none"/></svg>Over 65? You'll get a 10% discount.</li>
    </ul>
    <span class="web">www.qexdatalink.com.au</span>
  </div>
</section>

</body>
</html>
```